Web design for an intellectual property law practice

I need to design a simple landing page that may in the future expand to a full site. It should be very high tech focused.

Target Market(s)

Anyone seeking legal services

Industry/Entity Type

Legal

Number of Pages Required

2 page

Font styles to use
Other font styles liked:
• The same font as my logo

Colors
ec1f27

Requirements
Must have
• My logo (see attached).
Nice to have
• Open to ideas.

```html
<!DOCTYPE html>
<html lang="en">
<head>
<meta charset="utf-8">
<title>Northlight IP Law</title>
<link href="https://fonts.googleapis.com/css2?family=Raleway:wght@400;500;600;700;800&display=swap" rel="stylesheet">
<style>
:root{
  --red:#ec1f27;
  --red-deep:#c4121b;
  --ink:#222;
  --grey:#777;
  --line:#ddd;
  --paper:#f7f7f7;
  --black:#000;
  --white:#fff;
}
*{box-sizing:border-box;margin:0;padding:0}
html,body{width:1200px;height:1200px;overflow:hidden;background:var(--white);font-family:'Raleway',sans-serif}
.page{position:absolute;left:128px;top:24px;width:944px;height:1152px;box-shadow:0 0 14px rgba(90,60,110,.45);background:var(--paper)}
.abs{position:absolute}
.cx{transform:translateX(-50%);white-space:nowrap}

/* hero */
.hero{position:absolute;left:0;top:0;width:944px;height:369px;overflow:hidden;
  background:radial-gradient(ellipse 420px 260px at 420px 170px,#b3141c 0%,#7a0f14 45%,#2a0a0c 100%)}
.hero-art{position:absolute;inset:0;background:radial-gradient(circle 150px at 745px 170px,rgba(230,120,120,.35),rgba(0,0,0,0) 70%)}
.hero .kicker{top:115px;left:331px;color:var(--white);font-size:9px;font-weight:500}
.hero h1{top:124px;left:337px;color:var(--white);font-size:31px;font-weight:800;letter-spacing:.3px}
.hero .tag{top:162px;left:186px;width:305px;height:19px;background:var(--white);color:var(--red);font-size:8.5px;font-weight:500;display:flex;align-items:center;justify-content:center}
.hero .divider{top:202px;left:186px;width:305px;height:16px;display:flex;align-items:center;justify-content:center;gap:6px;color:var(--white);font-size:12px;font-weight:700}
.divider .rule{flex:1;height:3px;border-top:1px solid rgba(255,255,255,.8);border-bottom:1px solid rgba(255,255,255,.8)}
.hero .down{top:240px;left:324px}

/* nav */
.nav{position:absolute;left:0;top:369px;width:944px;height:50px;background:var(--white);border-bottom:1px solid var(--line)}
.brand{display:flex;flex-direction:column;align-items:center;gap:3px}
.brand .mark{border:1.5px solid currentColor;border-radius:50%}
.brand .name{font-weight:600;letter-spacing:.2px}
.nav .brand{left:215px;top:6px;color:var(--ink)}
.nav .brand .mark{width:22px;height:22px}
.nav .brand .name{font-size:8px}
.menu a{position:absolute;top:19px;font-size:6.5px;font-weight:700;color:#444;text-decoration:none;transform:translateX(-50%)}
.menu a.active{top:15px;background:var(--red-deep);color:var(--white);padding:5px 7px;border-radius:1px}

/* services */
.services{position:absolute;left:0;top:419px;width:944px;height:303px;background:var(--paper)}
.services .head{top:36px;left:472px;display:flex;align-items:center;gap:12px;font-size:13px;font-weight:700;color:var(--ink)}
.services .head em{font-style:normal;color:var(--red-deep)}
.services .headline{top:44px;height:1px;background:linear-gradient(90deg,rgba(0,0,0,0),var(--line))}
.services .lead{top:57px;left:472px;font-size:8px;color:var(--grey)}
.card{position:absolute;top:89px;width:170px;transform:translateX(-50%);text-align:center}
.card .icon{width:50px;height:50px;border-radius:50%;background:#333;margin:0 auto;display:flex;align-items:center;justify-content:center}
.card.featured .icon{background:var(--red-deep)}
.card h3{margin-top:15px;font-size:7px;font-weight:700;color:#333}
.card p{margin-top:8px;font-size:7px;line-height:12px;color:var(--grey)}
.card .more{display:inline-block;margin-top:8px;font-size:5px;font-weight:700;color:#888;border:1px solid var(--line);padding:3px 5px}
.card.featured .more{background:var(--red-deep);color:var(--white);border-color:var(--red-deep)}

/* footer */
.footer{position:absolute;left:0;top:722px;width:944px;height:136px;background:var(--black)}
.footer .brand{left:472px;top:12px;color:var(--white);transform:translateX(-50%)}
.footer .brand .mark{width:30px;height:30px}
.footer .brand .name{font-size:10px;font-weight:500}
.social{position:absolute;top:78px;left:338px;display:flex;gap:4px}
.social span{width:21px;height:20px;border:1px solid #777;border-radius:2px}
.social span.on{background:var(--red-deep);border-color:var(--red-deep)}

/* map + contact */
.locate{position:absolute;left:0;top:858px;width:944px;height:246px;background:linear-gradient(90deg,#e6e6e6 0%,#e2e2e2 38%,#b9b9b9 60%,#cfcfcf 80%,#dadada 100%)}
.contact{position:absolute;left:184px;top:34px;width:182px;height:172px;background:var(--white);padding:14px 10px 0}
.field{height:20px;border:1px solid var(--line);margin-bottom:9px;font-size:6px;font-style:italic;color:#aaa;padding:6px 8px}
.field.msg{height:58px;margin-bottom:12px}
.submit{height:19px;background:var(--red-deep);color:var(--white);font-size:6px;font-weight:700;display:flex;align-items:center;justify-content:center}
.pin{left:463px;top:100px}

.bottom{position:absolute;left:0;top:1104px;width:944px;height:48px;background:var(--black)}
.bottom .copy{top:26px;left:472px;color:var(--white);font-size:7px;font-weight:600}
.totop{position:absolute;left:462px;top:-10px;width:20px;height:20px;background:var(--red-deep);transform:rotate(45deg)}
.totop-arrow{position:absolute;left:468px;top:-3px}
</style>
</head>
<body>
<div class="page">

  <header class="hero">
    <div class="hero-art" role="img" aria-label="Dark red high-tech backdrop with circuit grid and glowing circular interface"></div>
    <p class="abs cx kicker">LOREM IPSUM DOLOR SIT AMET</p>
    <h1 class="abs cx">LOREM IPSUM DOL !</h1>
    <p class="abs tag">LOREM IPSUM DOLOR SIT AMET, CONSECTETUR ADIPISEIPSUM DOLOR</p>
    <div class="abs divider"><span class="rule"></span><span>◆ LOREM IPSUM DOLOR ◆</span><span class="rule"></span></div>
    <svg class="abs down" width="28" height="28" viewBox="0 0 28 28"><circle cx="14" cy="14" r="13" fill="none" stroke="#fff" stroke-width="1.6"/><path d="M8 11l6 6 6-6" fill="none" stroke="#fff" stroke-width="1.8"/></svg>
  </header>

  <nav class="nav">
    <div class="abs cx brand"><span class="mark"></span><span class="name">northlight iplaw</span></div>
    <div class="menu">
      <a style="left:428px">HOME</a>
      <a class="active" style="left:477px">PORTFOLIO</a>
      <a style="left:524px">BLOG</a>
      <a style="left:563px">PAGES</a>
      <a style="left:610px">FEATURES</a>
      <a style="left:666px">MEGA MENU</a>
      <a style="left:721px">CONTACT</a>
    </div>
    <svg class="abs" style="left:751px;top:20px" width="9" height="9" viewBox="0 0 9 9"><circle cx="5" cy="4" r="3" fill="none" stroke="#c4121b" stroke-width="1.2"/><path d="M3 6L1 8" stroke="#c4121b" stroke-width="1.2"/></svg>
  </nav>

  <section class="services">
    <div class="abs headline" style="left:205px;width:190px"></div>
    <div class="abs headline" style="left:550px;width:190px;transform:scaleX(-1)"></div>
    <h2 class="abs cx head"><span style="color:#c4121b;font-size:8px">◆</span><span>LOREM <em>IPSUM</em></span><span style="color:#c4121b;font-size:8px">◆</span></h2>
    <p class="abs cx lead">Lorem ipsum dolor sit amet, consectetur adipiscing elit. Lorem ipsum dolor sit amet.</p>

    <article class="card" style="left:275px">
      <div class="icon"><svg width="18" height="16" viewBox="0 0 18 16"><rect x="1" y="1" width="16" height="10" fill="none" stroke="#fff" stroke-width="2"/><path d="M6 15h6M9 11v4" stroke="#fff" stroke-width="2"/></svg></div>
      <h3>LOREM IPSUM</h3>
      <p>Proin in magna a ipsum viverra scelerisq enec turp.<br>Nunc vestibulum fringilla accumsan ornare quis.</p>
      <span class="more">READ MORE</span>
    </article>
    <article class="card featured" style="left:472px;top:91px">
      <div class="icon"><svg width="16" height="16" viewBox="0 0 16 16"><rect x="1" y="5" width="14" height="10" fill="#fff"/><circle cx="8" cy="4" r="3" fill="#fff"/></svg></div>
      <h3>LOREM IPSUM</h3>
      <p>Proin in magna a ipsum viverra scelerisq enec turp.<br>Nunc vestibulum fringilla accumsan ornare quis.</p>
      <span class="more">READ MORE</span>
    </article>
    <article class="card" style="left:669px;top:91px">
      <div class="icon"><svg width="18" height="18" viewBox="0 0 18 18"><circle cx="9" cy="9" r="7" fill="none" stroke="#fff" stroke-width="2.5"/><circle cx="9" cy="9" r="3" fill="none" stroke="#fff" stroke-width="2"/></svg></div>
      <h3>LOREM IPSUM</h3>
      <p>Proin in magna a ipsum viverra scelerisq enec turp.<br>Nunc vestibulum fringilla accumsan ornare quis.</p>
      <span class="more">READ MORE</span>
    </article>
  </section>

  <footer class="footer">
    <div class="abs brand"><span class="mark"></span><span class="name">northlight iplaw</span></div>
    <div class="social" aria-label="Social links">
      <span></span><span class="on"></span><span></span><span></span><span></span><span></span><span></span><span></span><span></span><span></span><span></span>
    </div>
  </footer>

  <section class="locate" role="img" aria-label="Street map of the New York metropolitan area showing the office location">
    <form class="contact">
      <div class="field">Name</div>
      <div class="field">Email Address</div>
      <div class="field msg">Message ...</div>
      <div class="submit">SUBMIT MESSAGE</div>
    </form>
    <svg class="abs pin" width="18" height="26" viewBox="0 0 18 26"><path d="M9 1a8 8 0 0 1 8 8c0 6-8 16-8 16S1 15 1 9a8 8 0 0 1 8-8z" fill="#333"/><circle cx="9" cy="9" r="3.2" fill="#fff"/></svg>
  </section>

  <div class="bottom">
    <div class="totop"></div>
    <svg class="totop-arrow" width="8" height="6" viewBox="0 0 8 6"><path d="M0 5l4-4 4 4z" fill="#fff"/></svg>
    <p class="abs cx copy">Copyright © 2019</p>
  </div>

</div>
</body>
</html>
```